Flowchart

I need a nice graphic that doesn't look like a stock word/ppt graphic to show the organization of our office. Example included. The idea to get across is that all of the units work together and feed into each other. I need this asap so will likely award tomorrow
Please use all text and if possible incorporate logo.
Design should be around 8.5 X 11 or smaller. Landscape vs. Protrait doesn't matter much.
A few more notes.
no larger than 81/2 by 11
Landscape preferred
Landscape preferred
Landscape

```html
<!DOCTYPE html>
<html lang="en">
<head>
<meta charset="utf-8">
<title>Northfield Biosciences – Graduate Education Structure</title>
<link href="https://fonts.googleapis.com/css2?family=Oswald:wght@500;600&family=Roboto+Condensed:wght@500&display=swap" rel="stylesheet">
<style>
  :root {
    --page: #ffffff;
    --charcoal: #575757;
    --slate: #b9c0c2;
    --crimson: #c8202a;
    --fold-light: #f1f1ef;
    --fold-mid: #d9d9d6;
    --fold-dark: #b4b4b1;
    --ink-light: #ffffff;
    --ink-dark: #3b3b3b;
    --brand: #4a4a4a;
  }
  html, body {
    margin: 0;
    padding: 0;
    width: 1200px;
    height: 848px;
    overflow: hidden;
    background: var(--page);
  }
  .chart {
    position: relative;
    width: 1200px;
    height: 848px;
  }
  .ribbon {
    position: absolute;
    inset: 0;
  }
  .brand {
    position: absolute;
    top: 52px;
    left: 660px;
    display: flex;
    align-items: center;
    gap: 12px;
    font-family: "Oswald", "Arial Narrow", sans-serif;
    font-weight: 500;
    font-size: 33px;
    letter-spacing: 0.5px;
    color: var(--brand);
  }
  .brand-dot {
    width: 14px;
    height: 14px;
    border-radius: 50%;
    background: var(--crimson);
  }
  .unit {
    position: absolute;
    display: flex;
    align-items: center;
  }
  .unit-title {
    font-family: "Oswald", "Arial Narrow", sans-serif;
    font-weight: 600;
    line-height: 1.2;
    margin: 0;
  }
  .unit-divider {
    align-self: stretch;
    border-left: 2px dotted currentColor;
    opacity: 0.7;
    margin: 14px 0;
  }
  .unit-list {
    list-style: none;
    margin: 0;
    padding: 0;
    font-family: "Roboto Condensed", "Arial Narrow", sans-serif;
    font-weight: 500;
    font-size: 17.5px;
    line-height: 1.25;
  }
  .unit-list li {
    position: relative;
  }
  .unit-list li::before {
    content: "";
    position: absolute;
    top: 5px;
    width: 8px;
    height: 8px;
    border-radius: 50%;
    background: currentColor;
  }

  /* Home programs */
  .unit--home {
    top: 125px; left: 265px; width: 830px; height: 194px;
    color: var(--ink-light);
  }
  .unit--home .unit-title {
    width: 210px; text-align: right; font-size: 27px; margin-right: 60px;
  }
  .unit--home .unit-list { margin-left: 28px; }
  .unit--home .unit-list li { padding-left: 22px; margin: 8px 0; }
  .unit--home .unit-list li::before { left: 2px; }

  /* Committee */
  .unit--committee {
    top: 360px; left: 265px; width: 735px; height: 192px;
    color: var(--ink-dark);
  }
  .unit--committee .unit-list {
    width: 332px; text-align: right; margin-right: 40px;
  }
  .unit--committee .unit-list li { padding-right: 22px; margin: 12px 0; }
  .unit--committee .unit-list li::before { right: 2px; }
  .unit--committee .unit-title {
    font-size: 29px; margin-left: 28px; line-height: 1.25;
  }

  /* Office */
  .unit--office {
    top: 592px; left: 130px; width: 880px; height: 194px;
    color: var(--ink-light);
  }
  .unit--office .unit-title {
    width: 310px; text-align: right; font-size: 27px; margin-right: 52px;
  }
  .unit--office .unit-list { margin-left: 22px; }
  .unit--office .unit-list li { padding-left: 22px; margin: 8px 0; }
  .unit--office .unit-list li::before { left: 2px; }
</style>
</head>
<body>
<main class="chart">
  <svg class="ribbon" width="1200" height="848" viewBox="0 0 1200 848" aria-hidden="true">
    <defs>
      <linearGradient id="fold-left" x1="0" y1="0" x2="1" y2="0">
        <stop offset="0" stop-color="var(--fold-mid)"/>
        <stop offset="0.55" stop-color="var(--fold-light)"/>
        <stop offset="1" stop-color="var(--fold-dark)"/>
      </linearGradient>
      <linearGradient id="fold-right" x1="0" y1="0" x2="1" y2="0">
        <stop offset="0" stop-color="var(--fold-dark)"/>
        <stop offset="0.45" stop-color="var(--fold-light)"/>
        <stop offset="1" stop-color="var(--fold-mid)"/>
      </linearGradient>
      <linearGradient id="band-slate" x1="0" y1="0" x2="1" y2="0">
        <stop offset="0" stop-color="#a9b0b2"/>
        <stop offset="0.5" stop-color="var(--slate)"/>
        <stop offset="1" stop-color="#c9cfd0"/>
      </linearGradient>
      <linearGradient id="band-crimson" x1="0" y1="0" x2="1" y2="0">
        <stop offset="0" stop-color="var(--crimson)"/>
        <stop offset="0.85" stop-color="var(--crimson)"/>
        <stop offset="1" stop-color="#a3161e"/>
      </linearGradient>
    </defs>
    <!-- folds -->
    <path class="fold fold--left" d="M265,125 L160,222 Q130,250 130,290 L130,440 Q130,470 160,490 L265,552 Z" fill="url(#fold-left)"/>
    <path class="fold fold--right" d="M990,360 Q1050,360 1085,420 L1125,500 Q1135,525 1135,560 L1135,650 Q1135,700 1090,735 L1010,786 L1010,592 L1000,552 Z" fill="url(#fold-right)"/>
    <path class="fold fold--top" d="M1095,60 Q1120,70 1120,110 L1120,300 Q1110,318 1095,318 Z" fill="var(--fold-light)"/>
    <!-- bands -->
    <rect class="band band--home" x="265" y="125" width="830" height="194" fill="var(--charcoal)"/>
    <path class="band band--committee" d="M265,360 L950,360 Q1000,360 1000,410 L1000,552 L265,552 Z" fill="url(#band-slate)"/>
    <rect class="band band--office" x="130" y="592" width="880" height="194" fill="url(#band-crimson)"/>
  </svg>

  <div class="brand"><span class="brand-dot"></span>NORTHFIELD BIOSCIENCES</div>

  <section class="unit unit--home">
    <h2 class="unit-title">Biosciences<br>Home Programs</h2>
    <span class="unit-divider"></span>
    <ul class="unit-list">
      <li>Supports students with department or program specific<br>degree progress and graduation requirements</li>
      <li>Administers program-specific core curriculum</li>
      <li>Eight departments and Six interdisciplinary programs</li>
    </ul>
  </section>

  <section class="unit unit--committee">
    <ul class="unit-list">
      <li>Administrative oversight of Biosciences admissions, curriculum and policies</li>
      <li>Forum for cross-program discussion and collaboration</li>
    </ul>
    <span class="unit-divider"></span>
    <h2 class="unit-title">Committee on Graduate<br>Admissions &amp; Policy<br>(CGAP)</h2>
  </section>

  <section class="unit unit--office">
    <h2 class="unit-title">Office of Graduate<br>Education (OGE)</h2>
    <span class="unit-divider"></span>
    <ul class="unit-list">
      <li>Promotes the academic, personal &amp; professional<br>development of all students through comprehensive<br>programs and services</li>
      <li>Advocates for the best possible training and<br>empowerment of all students</li>
      <li>Develops and administers Biosciences–wide,<br>interdisciplinary curriculum</li>
    </ul>
  </section>
</main>
</body>
</html>
```